A standard Business and Stock Market Website

We are looking for a well designed and attractive website design which deals on the day to day business activities and stock market performance across the globe.

A good reference website for my proposed website is http://marrowfinch.com and http://qpv.com

We are basically featuring the leading stock markets such as Pel varney stock market and others. The Business name is Tarn lane.
I require very bright colors such as blue, green, black, golden.

Easy nagivating of the website is require and the design should also be responsive on mobile devices.

Designs for three pages. The first design should be for the home page, the second for the Economy/ stockmarkets, Third, business and tech. The home image would also feature stocks, economy, business, tech.

```html
<!DOCTYPE html>
<html lang="en">
<head>
<meta charset="utf-8">
<title>Tarn Lane — Business &amp; Stock Markets</title>
<link href="https://fonts.googleapis.com/css2?family=Noto+Serif:wght@400;700&family=Roboto:wght@400;500;700&display=swap" rel="stylesheet">
<style>
:root{
  --blue:#3d7ef0;
  --blue-dark:#1f5fd0;
  --green:#5db624;
  --gold:#e0a613;
  --black:#111111;
  --ink:#222222;
  --muted:#777777;
  --line:#d6d6d6;
  --page:#efefed;
  --panel:#ffffff;
  --footer:#f7f7f7;
  --serif:"Noto Serif", Georgia, serif;
  --sans:"Roboto", Arial, sans-serif;
}
*{box-sizing:border-box;margin:0;padding:0}
html,body{width:1200px;height:3000px;overflow:hidden}
body{background:var(--page);font-family:var(--sans);color:var(--ink);position:relative}
.abs{position:absolute}
a{color:inherit;text-decoration:none}

.corp-strip{left:0;top:0;width:1200px;height:16px;background:var(--blue);color:#fff;font-size:9px;font-weight:700;padding:3px 0 0 162px;letter-spacing:.3px}
.ticker{left:0;top:16px;width:1200px;height:24px;background:var(--black);color:#fff;font-size:9px;display:flex;gap:28px;padding:7px 0 0 162px;white-space:nowrap}
.ticker .down{color:#ff6b6b}.ticker .up{color:#7fd36a}

.ad{left:330px;top:44px;width:540px;height:64px}
.ad-body{position:absolute;left:36px;top:4px;width:468px;height:56px;background:linear-gradient(180deg,#2b73c9,#1a4d96);border-top:4px solid #f08a1c;border-bottom:4px solid #f08a1c;display:flex;align-items:center;padding-left:110px;gap:30px}
.ad-title{color:#fff;font:700 17px var(--sans)}
.ad-title small{display:block;font:400 8px var(--sans);color:#cfe1ff}
.ad-btn{background:#f08a1c;color:#fff;font:700 9px var(--sans);padding:6px 12px}
.ad-icon{position:absolute;left:64px;top:12px;width:32px;height:32px;background:#f5a33a}

.brand{left:162px;top:126px;font:400 31px var(--serif);letter-spacing:1px;color:var(--black)}
.account{right:162px;top:122px;text-align:right;font:500 9px var(--sans);color:var(--black)}
.offer{right:162px;top:134px;font:700 13px var(--sans);color:var(--blue);letter-spacing:.3px}

.nav{left:162px;top:176px;width:876px;height:34px;background:var(--blue);display:flex;align-items:center}
.nav a{color:#fff;font:500 10px var(--sans);padding:0 10px;text-transform:uppercase}
.nav a:first-child{padding-left:18px}
.search{position:absolute;right:0;top:0;width:120px;height:34px;background:var(--black);color:#fff;font:500 9px var(--sans);display:flex;align-items:center;justify-content:space-between;padding:0 12px 0 18px}

.hero{left:162px;top:222px;width:554px;height:408px;background:radial-gradient(circle at 55% 35%,#3fa0ff 0%,#0f4ea8 45%,#061b45 100%)}
.hero h1{position:absolute;left:24px;bottom:32px;color:#fff;font:700 21px/1.35 var(--serif);letter-spacing:1px;text-transform:uppercase}
.hero-card{left:732px;top:222px;width:306px;height:408px;background:var(--panel)}
.tabs{display:flex;height:30px}
.tabs span{flex:1;display:flex;align-items:center;justify-content:center;font:400 10px var(--serif);text-transform:uppercase;border:1px solid #e3e3e3}
.tabs .on{background:var(--green);color:#fff;border-color:var(--green)}
.hero-photo{height:196px;background:linear-gradient(135deg,#8c6a4c,#c7a47a 55%,#b8451d)}
.hero-card .date{font:500 9px var(--sans);color:var(--muted);margin:20px 0 0 20px;text-transform:uppercase}
.hero-card h2{font:700 15px/1.45 var(--serif);margin:12px 20px 0;text-transform:uppercase;letter-spacing:.5px}
.hero-foot{position:absolute;left:20px;right:20px;bottom:22px;display:flex;justify-content:space-between;align-items:center}
.dots{display:flex;gap:14px}
.dots i{width:10px;height:10px;border-radius:50%;background:#b9c4d2;display:block}
.dots i:first-child{background:var(--blue)}
.like{font:500 9px var(--sans);color:var(--green)}

.partners{left:162px;top:650px;width:876px;height:54px;border-top:1px solid var(--line);border-bottom:1px solid var(--line);display:flex;align-items:center;justify-content:space-between;padding:0 36px}
.partners span{font:700 20px var(--serif);color:#8a8a8a}

.label{height:34px;padding:0 18px;display:flex;align-items:center;color:#fff;font:400 13px var(--serif);text-transform:uppercase;letter-spacing:.5px}
.gold{background:var(--gold)}.green{background:var(--green)}.blackl{background:var(--black)}.bluel{background:var(--blue)}.grey{background:#555}

.ocard{width:266px;height:230px;overflow:hidden}
.ocard .ph{height:100%}
.ocard .shade{position:absolute;left:0;right:0;bottom:0;height:108px;background:linear-gradient(180deg,rgba(0,0,0,0),rgba(0,0,0,.85))}
.ocard .tag{position:absolute;left:12px;bottom:78px}
.ocard h3{position:absolute;left:12px;right:12px;bottom:34px;color:#fff;font:400 14px/1.4 var(--sans)}
.ocard .meta{position:absolute;left:12px;bottom:12px;color:#fff}
.tag{display:inline-block;color:#fff;font:700 8px var(--sans);padding:3px 6px;text-transform:uppercase}
.tag.y{background:var(--gold)}.tag.g{background:var(--green)}.tag.b{background:var(--blue)}.tag.k{background:#444}
.meta{font:400 8px var(--sans);display:flex;gap:22px;align-items:center}
.meta span{display:flex;align-items:center;gap:6px}
.ico{width:9px;height:9px}

.chart{left:732px;top:780px;width:306px;height:200px;background:var(--panel);padding:14px 12px}
.chart h4{font:700 10px var(--sans)}
.chart small{font:400 7px var(--sans);color:var(--muted);position:absolute;right:44px;top:30px}

.feature-img{left:162px;top:1062px;width:554px;height:290px;background:linear-gradient(135deg,#cfd8dd,#f2f2f0 50%,#a9b8c4)}
.feature{left:162px;top:1374px;width:554px}
.feature h2{font:400 17px var(--serif);margin:8px 0 10px}
.feature p{font:400 9.5px/1.55 var(--sans);color:#666;margin-top:16px}

.item{left:162px;width:554px;height:126px}
.item .ph{position:absolute;left:0;top:0;width:190px;height:126px}
.item .txt{position:absolute;left:206px;top:0;right:0}
.item h4{font:700 10px var(--serif);margin:8px 0 10px}
.item .meta{color:#666}
.item p{font:400 9px/1.5 var(--sans);color:#777;margin-top:10px}

.rnews{left:732px;width:306px}
.rnews .ph{height:176px}
.rnews .tag{margin-top:10px}
.rnews h3{font:400 16px/1.35 var(--serif);margin-top:6px}
.rnews .meta{font-size:12px;gap:0;justify-content:space-between;padding-right:30px;margin-top:10px}
.rnews .meta .ico{width:13px;height:13px}

.pop{left:732px;width:306px;height:84px;border-bottom:1px solid var(--line)}
.pop .txt{position:absolute;left:0;top:0;width:190px}
.pop h4{font:400 11.5px/1.35 var(--serif);margin:8px 0 8px}
.pop .ph{position:absolute;right:0;top:0;width:110px;height:80px}
.pop .meta{font-size:8px;gap:16px}

.author{left:732px;top:2300px;width:306px;height:364px;background:var(--panel);border-top:4px solid var(--blue);padding:22px 18px}
.avatar{position:absolute;left:18px;top:26px;width:84px;height:84px;border-radius:50%;background:radial-gradient(circle,#d4a98a,#7a5a48)}
.author h5{position:absolute;left:118px;top:26px;font:700 13px var(--serif);text-transform:uppercase}
.author .bio{position:absolute;left:118px;top:48px;right:18px;font:400 9px/1.65 var(--sans);color:#555;text-align:justify}
.author blockquote{position:absolute;left:26px;right:26px;top:146px;text-align:center;font:400 18px/1.35 var(--serif);color:var(--black)}
.author .more{position:absolute;left:0;right:0;top:334px;text-align:center;font:400 11px var(--serif);color:var(--blue)}

.footer{left:0;top:2700px;width:1200px;height:240px;background:var(--footer)}
.fcol{position:absolute;top:30px;width:200px}
.fcol h6{font:400 14px var(--serif);margin-bottom:12px}
.fcol li{list-style:none;font:400 10px var(--sans);color:#333;line-height:22px;padding-left:4px}
.bottom{left:0;top:2940px;width:1200px;height:60px;display:flex;align-items:center;padding:0 162px 0 190px}
.social{display:flex;gap:18px}
.social i{width:11px;height:11px;border-radius:50%;background:#b9c4d2;display:block}
.social i:first-child{background:var(--blue)}
.copy{margin-left:auto;font:400 9px var(--sans);color:#333}
.copy b{margin-left:18px;font-weight:500}
</style>
</head>
<body>

<div class="abs corp-strip">PEL VARNEY, A HALDEN MEDIA COMPANY ▾</div>
<div class="abs ticker">
  <span>PVIA = 19762.60 <b class="down">-0.29%</b></span>
  <span>CRUDE OIL = 53.89 <b class="up">0.22%</b></span>
  <span>PVIA = 19762.60 <b class="down">-0.29%</b></span>
  <span>CRUDE OIL = 53.89 <b class="up">0.22%</b></span>
  <span>PVIA = 19762.60 <b class="down">-0.29%</b></span>
  <span>CRUDE OIL = 53.89 <b class="up">0.22%</b></span>
  <span>EURO = 53.89 <b class="up">0.22%</b></span>
</div>

<div class="abs ad">
  <svg width="540" height="64" class="abs" style="left:0;top:0"><polygon points="0,32 40,0 40,64" fill="#f08a1c"/><polygon points="540,32 500,0 500,64" fill="#f08a1c"/></svg>
  <div class="ad-body">
    <div class="ad-title">Cleanwave Utility<small>a handy tool for your PC cleanup</small></div>
    <div class="ad-btn">DOWNLOAD NOW</div>
  </div>
  <div class="ad-icon" role="img" aria-label="Software box illustration"></div>
</div>

<div class="abs brand">TARN LANE</div>
<div class="abs account">SUBSCRIBE NOW &nbsp;|&nbsp; SIGN IN</div>
<div class="abs offer">SPECIAL OFFER : JOIN NOW</div>

<nav class="abs nav">
  <a>Home</a><a>News</a><a>About</a><a>Investing</a><a>Actions</a><a>Real Money</a><a>More</a>
  <div class="search">SEARCH
    <svg width="10" height="10" viewBox="0 0 10 10"><circle cx="4" cy="4" r="3" fill="none" stroke="#fff" stroke-width="1.4"/><line x1="6.2" y1="6.2" x2="9.3" y2="9.3" stroke="#fff" stroke-width="1.4"/></svg>
  </div>
</nav>

<section class="abs hero" role="img" aria-label="Rising stacks of coins with an upward arrow on a blue stock graph">
  <h1>We are featuring the leading<br>stock markets</h1>
</section>

<aside class="abs hero-card">
  <div class="tabs"><span class="on">Ipsum</span><span>Dolor</span><span>Euro</span></div>
  <div class="hero-photo" role="img" aria-label="Business meeting in an office"></div>
  <div class="date">November 24, 2015</div>
  <h2>Lorium ipsum dolor amit is therefore always free from repetition</h2>
  <div class="hero-foot">
    <div class="dots"><i></i><i></i><i></i><i></i></div>
    <span class="like">LIKE 23 ♡</span>
  </div>
</aside>

<div class="abs partners">
  <span>Pel Varney</span>
  <span>Orbo News</span>
  <span>Cresta Daily</span>
  <span>Ferrowick</span>
  <span>Tarn Lane</span>
</div>

<div class="abs label gold" style="left:162px;top:734px">Stock Market Videos</div>
<div class="abs label blackl" style="left:732px;top:734px">Investments Stock</div>

<article class="abs ocard" style="left:162px;top:780px">
  <div class="ph" role="img" aria-label="Colleagues reviewing work at a desk" style="background:linear-gradient(135deg,#d9dde0,#8f9aa3)"></div>
  <div class="shade"></div>
  <span class="tag y">Share Market</span>
  <h3>Lorem Ipsum is simply dummy Text of the printing</h3>
  <div class="meta"><span><svg class="ico" viewBox="0 0 10 10"><path d="M1 1h8v6H4L1 9z" fill="#fff"/></svg>2 Comments</span><span><svg class="ico" viewBox="0 0 10 10"><rect x="1" y="2" width="8" height="7" fill="#fff"/></svg>July 11, 2016</span></div>
</article>
<article class="abs ocard" style="left:450px;top:780px">
  <div class="ph" role="img" aria-label="Business handshake" style="background:linear-gradient(135deg,#7ea7c9,#e9d6c0 60%,#3d4f66)"></div>
  <div class="shade"></div>
  <span class="tag y">Investment</span>
  <h3>Lorem Ipsum is simply dummy Text of the printing</h3>
  <div class="meta"><span><svg class="ico" viewBox="0 0 10 10"><path d="M1 1h8v6H4L1 9z" fill="#fff"/></svg>2 Comments</span><span><svg class="ico" viewBox="0 0 10 10"><rect x="1" y="2" width="8" height="7" fill="#fff"/></svg>July 11, 2016</span></div>
</article>

<div class="abs chart">
  <h4>Pel Varney Industrial Average</h4>
  <small>Jun 23, 4:00pm EDT</small>
  <svg width="282" height="150" viewBox="0 0 282 150" style="margin-top:6px">
    <g stroke="#e6e6e6" stroke-width="1">
      <line x1="0" y1="10" x2="236" y2="10"/><line x1="0" y1="34" x2="236" y2="34"/><line x1="0" y1="58" x2="236" y2="58"/>
      <line x1="0" y1="82" x2="236" y2="82"/><line x1="0" y1="106" x2="236" y2="106"/><line x1="0" y1="126" x2="236" y2="126"/>
      <line x1="62" y1="0" x2="62" y2="126"/><line x1="124" y1="0" x2="124" y2="126"/><line x1="186" y1="0" x2="186" y2="126"/>
    </g>
    <line x1="0" y1="66" x2="236" y2="66" stroke="#f0a080" stroke-dasharray="3 2"/>
    <polyline fill="none" stroke="#2a5caa" stroke-width="1.3" points="0,60 6,40 10,30 14,44 18,50 22,38 28,56 34,70 40,90 46,84 52,100 58,96 64,110 70,104 76,112 82,98 88,102 94,88 100,94 106,76 112,82 118,70 124,78 130,66 136,74 142,62 148,70 154,58 160,66 166,52 172,60 178,48 184,56 190,62 196,44 202,52 208,40 214,50 220,46 226,56 232,42 236,48"/>
    <g font-family="Roboto, Arial, sans-serif" font-size="8" fill="#444">
      <text x="240" y="13">18,200</text><text x="240" y="37">18,180</text><text x="240" y="61">18,160</text>
      <text x="240" y="85">18,140</text><text x="240" y="109">18,120</text><text x="240" y="129">18,100</text>
      <text x="6" y="140">10am</text><text x="56" y="140">12pm</text><text x="118" y="140">2pm</text><text x="180" y="140">4pm</text>
      <text x="0" y="122" font-size="7" fill="#888">© Quenmark</text>
      <line x1="110" y1="147" x2="122" y2="147" stroke="#f0a080"/><text x="126" y="150" font-size="7" fill="#888">Previous Close</text>
    </g>
  </svg>
</div>

<div class="abs label green" style="left:162px;top:1020px">Stock Market News</div>
<div class="abs label bluel" style="left:732px;top:996px">Latest News</div>

<div class="abs feature-img" role="img" aria-label="Three business people discussing documents at a table"></div>
<article class="abs feature">
  <span class="tag g">Market</span>
  <h2>Lorem Ipsum is simply dummy Text of the printing</h2>
  <div class="meta" style="color:#555"><span><svg class="ico" viewBox="0 0 10 10"><path d="M1 1h8v6H4L1 9z" fill="#333"/></svg>2 Comments</span><span><svg class="ico" viewBox="0 0 10 10"><rect x="1" y="2" width="8" height="7" fill="#333"/></svg>July 11, 2016</span></div>
  <p>Morbi iaculis vehicula enim. Proin enim lorem, faucibus et tempor id, dictum quis nisl. Nam nunc enim, consectetur vitae justo non, pharetra mattis purus. Nullam scelerisque nisl sem, sed vehicula tortor. Morbi iaculis vehicula enim. Proin enim lorem, faucibus et tempor id, dictum quis nisl. Nam nunc enim, consectetur vitae justo non, pharetra mattis purus. Nullam scelerisque nisl sem, sed vehicula tortor. Morbi iaculis vehicula enim. Proin enim lorem, faucibus et tempor id, dictum quis nisl. Nam nunc enim, consectetur vitae justo non, pharetra mattis purus. Nullam scelerisque nisl sem, sed vehicula tortor. Morbi iaculis vehicula enim. Proin enim lorem, faucibus et tempor id, dictum quis nisl. Nam nunc enim, consectetur vitae justo non, pharetra mattis purus. Nullam scelerisque nisl sem, sed vehicula tortor.</p>
</article>

<article class="abs item" style="top:1590px">
  <div class="ph" role="img" aria-label="Team of colleagues in an office" style="background:linear-gradient(135deg,#e8e6e2,#7b7f86)"></div>
  <div class="txt"><span class="tag g">Market</span><h4>Lorem Ipsum is simply dummy Text of the printing</h4>
  <div class="meta"><span><svg class="ico" viewBox="0 0 10 10"><path d="M1 1h8v6H4L1 9z" fill="#333"/></svg>2 Comments</span><span><svg class="ico" viewBox="0 0 10 10"><rect x="1" y="2" width="8" height="7" fill="#333"/></svg>July 11, 2016</span></div>
  <p>Morbi iaculis vehicula enim. Proin enim lorem, faucibus et tempor id, dictum quis nisl. Nam nunc enim, consectetur vitae justo non, pharetra mattis purus. Nullam scelerisque nisl sem, sed vehicula tortor. Morbi iaculis vehicula enim.</p></div>
</article>
<article class="abs item" style="top:1750px">
  <div class="ph" role="img" aria-label="Hand holding a glowing globe" style="background:radial-gradient(circle at 60% 45%,#5bb3ff,#0d2f66 70%)"></div>
  <div class="txt"><span class="tag g">Market</span><h4>Lorem Ipsum is simply dummy Text of the printing</h4>
  <div class="meta"><span><svg class="ico" viewBox="0 0 10 10"><path d="M1 1h8v6H4L1 9z" fill="#333"/></svg>2 Comments</span><span><svg class="ico" viewBox="0 0 10 10"><rect x="1" y="2" width="8" height="7" fill="#333"/></svg>July 11, 2016</span></div>
  <p>Morbi iaculis vehicula enim. Proin enim lorem, faucibus et tempor id, dictum quis nisl. Nam nunc enim, consectetur vitae justo non, pharetra mattis purus. Nullam scelerisque nisl sem, sed vehicula tortor. Morbi iaculis vehicula enim.</p></div>
</article>
<article class="abs item" style="top:1910px">
  <div class="ph" role="img" aria-label="Watering can pouring onto a money plant" style="background:linear-gradient(135deg,#f4f4f2,#b9c9a4 60%,#6f8f4c)"></div>
  <div class="txt"><span class="tag g">Market</span><h4>Lorem Ipsum is simply dummy Text of the printing</h4>
  <div class="meta"><span><svg class="ico" viewBox="0 0 10 10"><path d="M1 1h8v6H4L1 9z" fill="#333"/></svg>2 Comments</span><span><svg class="ico" viewBox="0 0 10 10"><rect x="1" y="2" width="8" height="7" fill="#333"/></svg>July 11, 2016</span></div>
  <p>Morbi iaculis vehicula enim. Proin enim lorem, faucibus et tempor id, dictum quis nisl. Nam nunc enim, consectetur vitae justo non, pharetra mattis purus. Nullam scelerisque nisl sem, sed vehicula tortor. Morbi iaculis vehicula enim.</p></div>
</article>
<article class="abs item" style="top:2070px">
  <div class="ph" role="img" aria-label="Printed charts and a pen on a desk" style="background:linear-gradient(135deg,#eef4fa,#9cc6ea 55%,#3f7fc0)"></div>
  <div class="txt"><span class="tag g">Market</span><h4>Lorem Ipsum is simply dummy Text of the printing</h4>
  <div class="meta"><span><svg class="ico" viewBox="0 0 10 10"><path d="M1 1h8v6H4L1 9z" fill="#333"/></svg>2 Comments</span><span><svg class="ico" viewBox="0 0 10 10"><rect x="1" y="2" width="8" height="7" fill="#333"/></svg>July 11, 2016</span></div>
  <p>Morbi iaculis vehicula enim. Proin enim lorem, faucibus et tempor id, dictum quis nisl. Nam nunc enim, consectetur vitae justo non, pharetra mattis purus. Nullam scelerisque nisl sem, sed vehicula tortor. Morbi iaculis vehicula enim.</p></div>
</article>
<article class="abs item" style="top:2230px">
  <div class="ph" role="img" aria-label="Businessman seated at a desk" style="background:linear-gradient(135deg,#f0f0ee,#9da3aa 60%,#2d3440)"></div>
  <div class="txt"><span class="tag g">Market</span><h4>Lorem Ipsum is simply dummy Text of the printing</h4>
  <div class="meta"><span><svg class="ico" viewBox="0 0 10 10"><path d="M1 1h8v6H4L1 9z" fill="#333"/></svg>2 Comments</span><span><svg class="ico" viewBox="0 0 10 10"><rect x="1" y="2" width="8" height="7" fill="#333"/></svg>July 11, 2016</span></div>
  <p>Morbi iaculis vehicula enim. Proin enim lorem, faucibus et tempor id, dictum quis nisl. Nam nunc enim, consectetur vitae justo non, pharetra mattis purus. Nullam scelerisque nisl sem, sed vehicula tortor. Morbi iaculis vehicula enim.</p></div>
</article>

<div class="abs label blackl" style="left:162px;top:2386px">Articles</div>
<article class="abs ocard" style="left:162px;top:2434px">
  <div class="ph" role="img" aria-label="Team leaning over a desk together" style="background:linear-gradient(135deg,#e6e9ec,#8d97a3)"></div>
  <div class="shade"></div>
  <span class="tag k">Articles</span>
  <h3>Lorem Ipsum is simply dummy Text of the printing</h3>
  <div class="meta"><span><svg class="ico" viewBox="0 0 10 10"><path d="M1 1h8v6H4L1 9z" fill="#fff"/></svg>2 Comments</span><span><svg class="ico" viewBox="0 0 10 10"><rect x="1" y="2" width="8" height="7" fill="#fff"/></svg>July 11, 2016</span></div>
</article>
<article class="abs ocard" style="left:450px;top:2434px">
  <div class="ph" role="img" aria-label="Businessman on a phone call" style="background:linear-gradient(135deg,#cfd7e0,#5a6678 60%,#1f2836)"></div>
  <div class="shade"></div>
  <span class="tag k">Articles</span>
  <h3>Lorem Ipsum is simply dummy Text of the printing</h3>
  <div class="meta"><span><svg class="ico" viewBox="0 0 10 10"><path d="M1 1h8v6H4L1 9z" fill="#fff"/></svg>2 Comments</span><span><svg class="ico" viewBox="0 0 10 10"><rect x="1" y="2" width="8" height="7" fill="#fff"/></svg>July 11, 2016</span></div>
</article>

<article class="abs rnews" style="top:1044px">
  <div class="ph" role="img" aria-label="Overhead view of people working at desks" style="background:linear-gradient(135deg,#f2f2f0,#b9bcbf 55%,#7a7f85)"></div>
  <span class="tag b">Market</span>
  <h3>Lorem Ipsum is simply dummy Text of the printing</h3>
  <div class="meta"><span><svg class="ico" viewBox="0 0 10 10"><path d="M1 1h8v6H4L1 9z" fill="#222"/></svg>2 Comments</span><span><svg class="ico" viewBox="0 0 10 10"><rect x="1" y="2" width="8" height="7" fill="#222"/></svg>July 11, 2016</span></div>
</article>
<article class="abs rnews" style="top:1340px">
  <div class="ph" role="img" aria-label="Financial newspaper tables with a pen" style="background:linear-gradient(135deg,#f3f3f3,#c8c8c8 60%,#8e8e8e)"></div>
  <span class="tag b">Market</span>
  <h3>Lorem Ipsum is simply dummy Text of the printing</h3>
  <div class="meta"><span><svg class="ico" viewBox="0 0 10 10"><path d="M1 1h8v6H4L1 9z" fill="#222"/></svg>2 Comments</span><span><svg class="ico" viewBox="0 0 10 10"><rect x="1" y="2" width="8" height="7" fill="#222"/></svg>July 11, 2016</span></div>
</article>
<article class="abs rnews" style="top:1632px">
  <div class="ph" role="img" aria-label="Stock exchange display board with red and blue figures" style="background:linear-gradient(135deg,#0d1f5c,#2a4fb0 45%,#a3222a)"></div>
  <span class="tag b">Market</span>
  <h3>Lorem Ipsum is simply dummy Text of the printing</h3>
  <div class="meta"><span><svg class="ico" viewBox="0 0 10 10"><path d="M1 1h8v6H4L1 9z" fill="#222"/></svg>2 Comments</span><span><svg class="ico" viewBox="0 0 10 10"><rect x="1" y="2" width="8" height="7" fill="#222"/></svg>July 11, 2016</span></div>
</article>

<div class="abs label grey" style="left:732px;top:1940px">Most Popular Articles</div>
<article class="abs pop" style="top:1990px">
  <div class="txt"><span class="tag k">Article</span><h4>Lorem Ipsum is simply dummy Text of the printing</h4>
  <div class="meta"><span><svg class="ico" viewBox="0 0 10 10"><path d="M1 1h8v6H4L1 9z" fill="#222"/></svg>2 Comments</span><span><svg class="ico" viewBox="0 0 10 10"><rect x="1" y="2" width="8" height="7" fill="#222"/></svg>July 11, 2016</span></div></div>
  <div class="ph" role="img" aria-label="Two businessmen shaking hands" style="background:linear-gradient(135deg,#eef0f2,#6d7580)"></div>
</article>
<article class="abs pop" style="top:2090px">
  <div class="txt"><span class="tag k">Article</span><h4>Lorem Ipsum is simply dummy Text of the printing</h4>
  <div class="meta"><span><svg class="ico" viewBox="0 0 10 10"><path d="M1 1h8v6H4L1 9z" fill="#222"/></svg>2 Comments</span><span><svg class="ico" viewBox="0 0 10 10"><rect x="1" y="2" width="8" height="7" fill="#222"/></svg>July 11, 2016</span></div></div>
  <div class="ph" role="img" aria-label="Businessman in front of a marketing chalkboard" style="background:linear-gradient(135deg,#22303d,#3f5566 60%,#1a1f26)"></div>
</article>
<article class="abs pop" style="top:2188px;border-bottom:none">
  <div class="txt"><span class="tag k">Article</span><h4>Lorem Ipsum is simply dummy Text of the printing</h4>
  <div class="meta"><span><svg class="ico" viewBox="0 0 10 10"><path d="M1 1h8v6H4L1 9z" fill="#222"/></svg>2 Comments</span><span><svg class="ico" viewBox="0 0 10 10"><rect x="1" y="2" width="8" height="7" fill="#222"/></svg>July 11, 2016</span></div></div>
  <div class="ph" role="img" aria-label="Smiling team of professionals" style="background:linear-gradient(135deg,#f4f4f4,#9aa0a8)"></div>
</article>

<aside class="abs author">
  <div class="avatar" role="img" aria-label="Author portrait"></div>
  <h5>Jhon Deo</h5>
  <p class="bio">Lorem Ipsum which looks reasonable. The generated Lorem Ipsum is therefore always free from repetition, injected humour, or non-characteristic words.</p>
  <blockquote>" Nam libero tempore, cum soluta nobis est eligendi optio cumque nihil impedit quo minus id quod maxime placeat facere possimus "</blockquote>
  <a class="more">~ Read more</a>
</aside>

<footer class="abs footer">
  <div class="fcol" style="left:190px"><h6>Membership</h6><ul><li>Lorium ipsum</li><li>Finibus</li><li>Bonorum</li><li>Malorum</li><li>Culpa qui</li><li>Consequatur</li><li>Nam libero</li></ul></div>
  <div class="fcol" style="left:408px"><h6>Navigations</h6><ul><li>Home</li><li>News</li><li>About Us</li><li>Investings</li><li>Actions</li><li>Real Money</li><li>More...</li></ul></div>
  <div class="fcol" style="left:618px"><h6>Subscriptions</h6><ul><li>Lorium ipsum</li><li>Finibus</li><li>Bonorum</li><li>Malorum</li><li>Culpa qui</li><li>Consequatur</li><li>Nam libero</li></ul></div>
  <div class="fcol" style="left:852px"><h6>Stay Connected</h6><ul><li>Lorium ipsum</li><li>Finibus</li><li>Bonorum</li><li>Malorum</li><li>Culpa qui</li><li>Consequatur</li><li>Nam libero</li></ul></div>
</footer>
<div class="abs bottom">
  <div class="social"><i></i><i></i><i></i><i></i></div>
  <div class="copy">Copyrights © 2016, www.companyname.com. All Rights Reserved. <b>TL</b></div>
</div>

</body>
</html>
```